Packaging for a new tea company

Hi guys we need a new packaging design for a tea company we are starting

Our competitors are leafora, zip an brew

I have uploaded pictures of our competitors for you to see the sample
The label need to be catchy

Our brand is called #JoinVividLeaf
We need two packaging designs one for Zest Brew and one for calmora

Detox - slim - cleanse

Also needs to says 14 Day Brewreset

Target Market(s)

Young people

Industry/Entity Type

It Company

Colors
000000

Requirements
Must have
• #joinvividleaf
Nice to have
• Herbal tea supplement 50gram
• Max label size 13.5cm x 16.5 cm
• Personally I like the paper brown bag as it looks like a higher quality and as the label is a sticker I think this would make the product look a lot better
Should not have
• Nothing

```html
<!DOCTYPE html>
<html lang="en">
<head>
<meta charset="utf-8">
<title>#JoinVividLeaf – Zest Brew Label</title>
<link rel="stylesheet" href="https://fonts.googleapis.com/css2?family=Neucha&family=Oswald:wght@400;600;700&display=swap">
<style>
  :root {
    --backdrop: #c59a68;
    --band-green: #6c9f2e;
    --band-text: #d9e8c6;
    --body-green: #d2e2bd;
    --body-green-soft: #dfeacf;
    --seal-fill: #eef2e7;
    --ink: #141414;
    --accent: #6aa12c;
  }
  html, body {
    margin: 0;
    width: 1200px;
    height: 900px;
    overflow: hidden;
    background: var(--backdrop);
  }
  .label {
    position: absolute;
    left: 267px;
    top: 100px;
    width: 666px;
    height: 750px;
    background: var(--body-green);
    font-family: "Oswald", sans-serif;
    color: var(--ink);
  }
  .leaf-pattern {
    position: absolute;
    left: 0; top: 96px;
    width: 100%; height: 518px;
    background: radial-gradient(ellipse at 50% 40%, var(--body-green-soft), var(--body-green) 75%);
  }
  .top-band, .bottom-band {
    position: absolute;
    left: 0;
    width: 100%;
    background: var(--band-green);
    color: var(--band-text);
    font-family: "Neucha", cursive;
  }
  .top-band { top: 0; height: 96px; }
  .bottom-band {
    bottom: 0; height: 136px;
    display: flex; align-items: center; justify-content: center;
  }
  .top-band .duration, .top-band .program {
    position: absolute;
    top: 18px;
    font-size: 50px;
    letter-spacing: 3px;
  }
  .top-band .duration { left: 40px; }
  .top-band .program { right: 40px; }
  .benefits {
    font-size: 52px;
    letter-spacing: 4px;
  }
  .brand-seal {
    position: absolute;
    left: 215px;
    top: -81px;
    width: 236px;
    height: 236px;
    box-sizing: border-box;
    border-radius: 50%;
    border: 8px solid var(--band-green);
    background: var(--seal-fill);
    display: flex; align-items: center; justify-content: center;
  }
  .brand-seal .brand-name {
    font-family: "Neucha", cursive;
    font-size: 46px;
    color: var(--accent);
    letter-spacing: 1px;
  }
  .hashtag {
    position: absolute;
    left: 30px;
    top: 218px;
    font-family: "Oswald", sans-serif;
    font-weight: 700;
    font-size: 250px;
    line-height: 1;
    color: var(--accent);
  }
  .headline {
    position: absolute;
    left: 200px;
    top: 232px;
    margin: 0;
    font-weight: 400;
    font-size: 100px;
    line-height: 1.08;
    letter-spacing: 2px;
    text-transform: uppercase;
  }
  .headline .accent-word { color: var(--accent); font-weight: 600; }
  .product-type, .net-weight {
    position: absolute;
    top: 578px;
    font-weight: 600;
    font-size: 22px;
    letter-spacing: -0.3px;
  }
  .product-type { left: 55px; }
  .net-weight { right: 60px; }
  .cup-icon {
    position: absolute;
    left: 375px;
    top: 548px;
    width: 64px;
    height: 64px;
  }
</style>
</head>
<body>
  <div class="label">
    <div class="leaf-pattern" role="img" aria-label="Faint pale tea leaf pattern"></div>

    <div class="top-band">
      <span class="duration">14 days</span>
      <span class="program">detox</span>
    </div>

    <div class="brand-seal">
      <span class="brand-name">zest brew</span>
    </div>

    <span class="hashtag">#</span>
    <h1 class="headline">Join <span class="accent-word">Vivid</span><br>Leaf</h1>

    <span class="product-type">HERBAL TEA SUPPLEMENT</span>
    <svg class="cup-icon" viewBox="0 0 64 64" aria-hidden="true">
      <path d="M14 30 h30 v6 a15 15 0 0 1 -30 0 z" fill="#141414"/>
      <path d="M44 33 a7 7 0 0 1 0 12" fill="none" stroke="#141414" stroke-width="4"/>
      <rect x="12" y="54" width="34" height="4" rx="2" fill="#141414"/>
      <path d="M29 27 C22 20 22 12 28 6 C34 13 34 20 29 27 z" fill="#6aa12c"/>
      <path d="M31 27 C34 18 42 15 50 16 C47 24 40 28 31 27 z" fill="#6aa12c"/>
    </svg>
    <span class="net-weight">50GRAM</span>

    <div class="bottom-band">
      <span class="benefits">detox~slim~clense</span>
    </div>
  </div>
</body>
</html>
```